Book Cover Design Project

NOTE. I need the design in four days of posting this!

This will be the cover of my first book, WALK THE HIGH LINE -
purpose at work in the modern company. The book explains defines what Purpose and Meaning is, and how to use it in business. I have included the first chapter to provide a background.

I want the core colours to be black and white, and use the colours Violet, Cerulean Blue Extra Pale (powder blue), Cadmium Lemon (flouro yellow). I plan on using this design as the basis for future books in the WALK THE HIGH LINE series, where the yellow is carried through but the violet and blue colours changing.

This is a spiritual business book without using any spiritual language. It is strongly masculine and direct in its nature.

What I am looking for is something Remarkable that captures my reader immediately. My reader is a seeker. He/she is an entrepreneur perhaps looking to setup a new venture and looking for new and better ways of doing things, or he/she may be a small/medium business owner perhaps bored looking for more meaning in personal and business life), or the corporate person who is looking to get out and do something new. Age 35-50.
Updates

Hi I want to correct the paper size. It is "C Format" (trade paperbacks) are 135mm x 216mm (5.32" x 8.51").

Thks

Reason: A deadline has changed which means the completion of this book cover is less time-critical.

This is a business book that introduces new concepts, such as Purpose. Although it is based on spiritual principals  it is using normal business language when explaining what Purpose is, and how businesses can identify it and use it to be more successful.

If there is a border between a self-help and a business book, this book sits close to the border but markedly on the business side.

Hi I want to confirm the book size. The book size I require is the Australian C Format, which measures 153mm W x 234mm H. 

Sorry for any confusion

Reason: Hi I have extended the deadline as I want to be able to print prospective covers and see how they look like in a bookshop next to other covers.

Reason: To allow for final negotiations.

Industry/Entity Type

Business

```html
<!DOCTYPE html>
<html lang="en">
<head>
<meta charset="utf-8">
<title>Walk the High Line — Book Cover</title>
<link rel="stylesheet" href="https://fonts.googleapis.com/css2?family=Teko:wght@400;600&family=Exo+2:wght@800&display=swap">
<style>
  :root {
    --ink: #0b0b0b;
    --glow: #4a4a4a;
    --powder-blue: #a6d8fb;
    --white: #ffffff;
    --lemon: #f3fb45;
    --violet: #3a1ee6;
  }
  * { margin: 0; padding: 0; box-sizing: border-box; }
  html, body {
    width: 784px;
    height: 1200px;
    overflow: hidden;
    background: var(--ink);
  }
  .cover {
    position: relative;
    width: 784px;
    height: 1200px;
    overflow: hidden;
    background:
      radial-gradient(ellipse 420px 520px at 50% 26%, var(--glow) 0%, #242424 45%, var(--ink) 85%);
    font-family: "Teko", "Arial Narrow", sans-serif;
    color: var(--white);
  }
  .title {
    position: absolute;
    top: 0;
    left: 0;
    width: 784px;
    height: 880px;
  }
  .title svg { display: block; width: 784px; height: 880px; }
  .title text {
    font-family: "Teko", "Arial Narrow", sans-serif;
    font-weight: 600;
    text-anchor: middle;
  }
  .title-walk { fill: var(--powder-blue); }
  .title-the { fill: var(--white); }
  .title-high-line { fill: var(--lemon); }
  .rule {
    position: absolute;
    left: 123px;
    width: 545px;
    height: 3px;
    background: var(--white);
  }
  .rule-top { top: 888px; }
  .rule-bottom { top: 980px; }
  .subtitle {
    position: absolute;
    top: 910px;
    left: 100px;
    width: 584px;
    text-align: center;
    font-weight: 400;
    font-size: 42px;
    line-height: 1;
    letter-spacing: 1px;
    white-space: nowrap;
    color: var(--white);
  }
  .author {
    position: absolute;
    top: 1094px;
    left: 0;
    width: 100%;
    text-align: center;
    font-family: "Exo 2", "Arial Black", sans-serif;
    font-weight: 800;
    font-size: 36px;
    letter-spacing: 27px;
    padding-left: 27px;
    white-space: nowrap;
    color: var(--violet);
  }
</style>
</head>
<body>
  <main class="cover">
    <h1 class="title" aria-label="Walk the High Line">
      <svg viewBox="0 0 784 880" aria-hidden="true">
        <text class="title-walk" x="392" y="352" font-size="459" textLength="520" lengthAdjust="spacingAndGlyphs">WALK</text>
        <text class="title-the" x="392" y="695" font-size="473" textLength="380" lengthAdjust="spacingAndGlyphs">THE</text>
        <text class="title-high-line" x="392" y="858" font-size="135" textLength="406" lengthAdjust="spacingAndGlyphs">HIGH LINE</text>
      </svg>
    </h1>
    <div class="rule rule-top"></div>
    <p class="subtitle">purpose at work in the modern company</p>
    <div class="rule rule-bottom"></div>
    <p class="author">Mikael Strand</p>
  </main>
</body>
</html>
```